Labor Day Sale Website Banner For High End Jewelry Website

We need a banner for our website (brindlyx.com) for a Labor Day Sale. The banner should be a size 1187 × 400. I have included a few pieces of jewelry to be included in the banner (do not need to use all, can use just some). The banner should say:
"Labor Day Sale"
"Save 15% on Everything!"
Use Promo Code: HALCYON

Target Market(s)

Affluent Female Consumers

Industry/Entity Type

Jewelry

Colors

Designer to choose colors to be used in the design.

```html
<!DOCTYPE html>
<html lang="en">
<head>
<meta charset="utf-8">
<title>Labor Day Sale – brindlyx.com</title>
<link rel="stylesheet" href="https://fonts.googleapis.com/css2?family=Great+Vibes&family=Josefin+Sans:ital,wght@0,300;1,300&display=swap">
<style>
  :root {
    --satin-light: #fbfbfa;
    --satin-mid: #ecebea;
    --satin-shadow: #d9d8d6;
    --ink: #141414;
    --gold: #c9a23a;
    --gold-deep: #8c6a1f;
    --amethyst: #5b3a6e;
    --amethyst-deep: #3b2146;
    --sapphire: #6e6fb4;
    --opal: #3f9c9a;
    --opal-deep: #2b5f6e;
  }
  html, body {
    margin: 0;
    padding: 0;
    width: 1200px;
    height: 404px;
    overflow: hidden;
    background: var(--satin-light);
  }
  .banner {
    position: relative;
    width: 1200px;
    height: 404px;
    overflow: hidden;
  }
  .satin-backdrop {
    position: absolute;
    inset: 0;
    background:
      radial-gradient(ellipse 420px 140px at 640px 60px, var(--satin-shadow), transparent 70%),
      radial-gradient(ellipse 500px 160px at 760px 300px, var(--satin-mid), transparent 70%),
      linear-gradient(160deg, var(--satin-mid) 0%, var(--satin-light) 35%, var(--satin-mid) 60%, var(--satin-light) 100%);
  }
  .jewel {
    position: absolute;
    border-radius: 18px;
  }
  .jewel--gold-earrings {
    left: 34px; top: 38px; width: 210px; height: 88px;
    background: linear-gradient(135deg, #f3d35a, var(--gold) 55%, var(--gold-deep));
  }
  .jewel--flower-earrings {
    left: 30px; top: 148px; width: 216px; height: 98px;
    border-radius: 48px;
    background: linear-gradient(120deg, #7a55a8, var(--sapphire) 40%, #c55a8f 70%, var(--sapphire));
  }
  .jewel--opal-earrings {
    left: 40px; top: 272px; width: 200px; height: 100px;
    border-radius: 50px;
    background: linear-gradient(135deg, var(--opal), var(--opal-deep) 60%, #4fb59a);
  }
  .jewel--amethyst-ring {
    left: 908px; top: 92px; width: 252px; height: 278px;
    border-radius: 60px 70px 60px 80px;
    background:
      radial-gradient(ellipse 95px 110px at 100px 130px, var(--amethyst), var(--amethyst-deep) 80%, transparent 100%),
      linear-gradient(135deg, #d6b25a, var(--gold) 50%, var(--gold-deep));
  }
  .sale-title {
    position: absolute;
    left: 300px;
    top: 84px;
    margin: 0;
    font-family: "Great Vibes", cursive;
    font-weight: 400;
    font-size: 100px;
    line-height: 1;
    color: var(--ink);
    white-space: nowrap;
  }
  .sale-offer {
    position: absolute;
    left: 298px;
    top: 274px;
    margin: 0;
    font-family: "Josefin Sans", sans-serif;
    font-weight: 300;
    font-size: 38px;
    line-height: 48px;
    color: var(--ink);
    white-space: nowrap;
  }
  .sale-offer__headline { display: block; font-style: italic; }
  .sale-offer__code { display: block; }
</style>
</head>
<body>
  <main class="banner">
    <div class="satin-backdrop" role="img" aria-label="Soft white draped satin fabric background"></div>

    <div class="jewel jewel--gold-earrings" role="img" aria-label="Pair of hammered yellow gold earrings"></div>
    <div class="jewel jewel--flower-earrings" role="img" aria-label="Pair of flower earrings set with amethyst, sapphire and pink tourmaline petals and a diamond centre"></div>
    <div class="jewel jewel--opal-earrings" role="img" aria-label="Pair of domed opal mosaic earrings in gold"></div>
    <div class="jewel jewel--amethyst-ring" role="img" aria-label="Large cushion-cut amethyst cocktail ring in textured gold leaf setting"></div>

    <h1 class="sale-title">Labor Day Sale</h1>
    <p class="sale-offer">
      <span class="sale-offer__headline">Save 15% on Everything!</span>
      <span class="sale-offer__code">Use Promo Code: HALCYON</span>
    </p>
  </main>
</body>
</html>
```